Information flyer for 5 day treatment flyer

I am wanting a double sided flyer for my next 5 day treatment program for addictions. I have included the copy for the flyer as an attachment.
I have also included a drop box link to my brand guidelines and my logos. The logo I prefer is the grey horse with the words Willowmere Collective under.
https://www.filecrate.example/sh/k2jtq7wn3xb5lp1/BBQr9TzLm4Kd7c8NpWvY2hsXe?dl=0

https://www.filecrate.example/s/qm8vz2kt6bw9rc4/WILLOWMERE%20COLLECTIVE%20%7C%20Brand%20Identity%20Guidelines.pdf?dl=0
I have also included a copy of an existing flyer which I like very much and a documant with the copy.
https://www.filecrate.example/sh/t7wbn3kx9zq1mv5/CCRt2pLw8-nZ4Kj7FyTuGHs_b?dl=0

I prefer simple, elegant designs please. The design needs to show my clients that I know what I am doing and I am trust worthy and a skilled professional.

Here is the drop box link to the images I have selected for this program. The tones in the images I have selected are orange/red. Please feel free to pick what you think works well.
https://www.filecrate.example/sh/mrq5jv82lnc0tfw/DDDhW392Bx6Lp88_Q7KcZnRye?dl=0

Many thanks
Marisol

```html
<!DOCTYPE html>
<html lang="en">
<head>
<meta charset="utf-8">
<title>Behind Closed Doors – 5 Day Intensive Treatment Program</title>
<link href="https://fonts.googleapis.com/css2?family=Bebas+Neue&family=Lato:wght@300;400;700&display=swap" rel="stylesheet">
<style>
  :root {
    --navy: #14253c;
    --navy-deep: #10203a;
    --cream: #e9e2d4;
    --cream-light: #f6f2ea;
    --beige-band: #e3dac6;
    --taupe: #a39d92;
    --taupe-dark: #8f897e;
    --ink: #2b2b2b;
    --ink-soft: #4a4a4a;
    --heading-grey: #9c968b;
    --white: #ffffff;
    --rule: #c9c2b4;
  }
  * { box-sizing: border-box; margin: 0; padding: 0; }
  html, body { width: 1200px; height: 1200px; overflow: hidden; }
  body {
    background: radial-gradient(ellipse at 50% 40%, #1b2f4a 0%, var(--navy) 55%, var(--navy-deep) 100%);
    font-family: "Lato", Arial, sans-serif;
    color: var(--ink);
    position: relative;
  }
  .brand-header {
    position: absolute; top: 118px; left: 0; width: 1200px;
    display: flex; align-items: center; justify-content: center; gap: 14px;
  }
  .brand-dot { width: 18px; height: 18px; border-radius: 50%; background: var(--taupe); }
  .brand-name {
    font-family: "Lato", Arial, sans-serif; font-weight: 300;
    font-size: 20px; letter-spacing: 5px; color: var(--taupe);
  }
  .page {
    position: absolute; top: 264px; width: 563px; height: 795px;
    background: linear-gradient(180deg, var(--cream) 0%, var(--cream) 55%, var(--white) 100%);
    box-shadow: 0 6px 18px rgba(0,0,0,.35);
    overflow: hidden;
  }
  .page::before, .page::after {
    content: ""; position: absolute; left: 0; width: 100%; height: 8px; background: var(--taupe);
  }
  .page::before { top: 0; }
  .page::after { bottom: 0; }
  .page--front { left: 21px; }
  .page--back { left: 616px; }
  .bebas { font-family: "Bebas Neue", "Oswald", sans-serif; font-weight: 400; }
  .abs { position: absolute; }

  /* front */
  .program-tag {
    left: 261px; top: 26px; width: 302px; height: 22px; background: var(--taupe);
    color: var(--white); font-size: 21px; line-height: 23px; text-align: center; letter-spacing: .3px;
  }
  .corner-brand { left: 14px; top: 44px; display: flex; align-items: center; gap: 5px; }
  .corner-brand .dot { width: 9px; height: 9px; border-radius: 50%; background: var(--ink); }
  .corner-brand span { font-size: 10px; font-weight: 700; color: var(--ink); letter-spacing: 1px; line-height: 1.1; }
  .hero-photo {
    left: 231px; top: 62px; width: 332px; height: 326px;
    background:
      linear-gradient(90deg, var(--cream) 0%, rgba(233,226,212,0) 30%),
      linear-gradient(180deg, rgba(233,226,212,0) 70%, var(--cream) 100%),
      radial-gradient(ellipse at 55% 45%, #6e6558 0%, #8f8b78 40%, #b3ad99 75%, #d7d0c0 100%);
  }
  .frame-line { position: absolute; background: var(--white); box-shadow: 0 1px 3px rgba(0,0,0,.12); }
  .title { left: 44px; top: 112px; font-size: 88px; line-height: 68px; letter-spacing: 1px; }
  .title span { display: block; }
  .title .light { color: var(--white); text-shadow: 0 2px 5px rgba(0,0,0,.25); }
  .title .dark { color: var(--ink); }
  .tagline { left: 44px; top: 374px; font-size: 21px; line-height: 22px; color: var(--heading-grey); }
  .info-table { left: 23px; top: 456px; width: 521px; }
  .info-row { display: flex; border-bottom: 1px solid var(--white); }
  .info-row dt {
    width: 158px; flex: none; background: var(--taupe); color: var(--white);
    padding: 16px 10px 8px 11px; font-size: 17px; line-height: 17px;
  }
  .info-row dt.small { font-size: 12.5px; line-height: 12.5px; padding-top: 14px; }
  .info-row dd {
    padding: 4px 0 6px 10px; font-size: 9.4px; line-height: 10.4px; color: var(--ink-soft);
    border-bottom: 1px solid var(--rule);
  }
  .info-row dd b { color: var(--ink); }

  /* back */
  .will-heading { left: 42px; top: 49px; font-size: 24px; line-height: 23px; color: var(--heading-grey); }
  .child-photo {
    left: 35px; top: 224px; width: 185px; height: 130px;
    background:
      linear-gradient(180deg, var(--cream) 0%, rgba(233,226,212,0) 30%),
      linear-gradient(270deg, var(--cream) 0%, rgba(233,226,212,0) 35%),
      radial-gradient(ellipse at 45% 60%, #7b7468 0%, #a09884 45%, #c7bfae 80%);
  }
  .outcomes { left: 205px; top: 45px; width: 352px; list-style: none; }
  .outcomes li {
    position: relative; padding-left: 12px; font-size: 10px; line-height: 10.6px;
    color: var(--ink); margin-bottom: 4.5px;
  }
  .outcomes li::before, .bullets li::before {
    content: ""; position: absolute; left: 1px; top: 3.5px; width: 4px; height: 4px; border-radius: 50%; background: var(--ink);
  }
  .back-corner-brand { left: 440px; top: 318px; display: flex; align-items: center; gap: 5px; }
  .back-corner-brand .dot { width: 9px; height: 9px; border-radius: 50%; background: var(--ink); }
  .back-corner-brand span { font-size: 10px; font-weight: 700; color: var(--ink); letter-spacing: 1px; }
  .card {
    position: absolute; top: 385px; width: 238px; height: 267px; background: var(--white);
    box-shadow: 0 2px 6px rgba(0,0,0,.18); padding: 10px 0 0 0;
  }
  .card--details { left: 33px; }
  .card--inclusions { left: 297px; }
  .card h3 { font-size: 22px; line-height: 23px; color: var(--heading-grey); padding: 0 17px; }
  .schedule { background: var(--beige-band); margin: 6px 5px 6px 5px; padding: 5px 12px; border-collapse: collapse; width: calc(100% - 10px); }
  .schedule td { font-size: 9.6px; line-height: 10.6px; font-weight: 700; color: var(--ink); padding: 0; }
  .card p { font-size: 9.4px; line-height: 10.4px; color: var(--ink-soft); padding: 4px 17px 0; }
  .card p b { color: var(--ink); }
  .bullets { list-style: none; padding: 2px 10px 2px 17px; }
  .bullets li { position: relative; padding-left: 10px; font-size: 9.3px; line-height: 10.4px; color: var(--ink); }
  .price { background: var(--beige-band); margin: 4px 6px 6px 17px; padding: 3px 6px; font-size: 10px; font-weight: 700; }
  .footer-band {
    left: 0; top: 683px; width: 563px; height: 100px; background: var(--navy);
  }
  .footer-brand { left: 32px; top: 44px; display: flex; align-items: center; gap: 8px; }
  .footer-brand .dot { width: 12px; height: 12px; border-radius: 50%; background: var(--taupe); }
  .footer-brand span { font-size: 10.5px; letter-spacing: 2.5px; color: var(--taupe); font-weight: 300; }
  .company { left: 299px; top: 18px; color: var(--white); }
  .company h4 { font-size: 13px; font-weight: 700; margin-bottom: 6px; }
  .company p { font-size: 10.6px; line-height: 10.6px; display: flex; align-items: center; gap: 5px; }
  .company p svg { width: 9px; height: 9px; flex: none; }
  .company p.indent { padding-left: 14px; }
</style>
</head>
<body>

<header class="brand-header">
  <span class="brand-dot"></span>
  <span class="brand-name">WILLOWMERE COLLECTIVE</span>
</header>

<!-- Front page -->
<section class="page page--front">
  <div class="abs program-tag bebas">5 Days Intensive Treatment Program</div>
  <div class="abs corner-brand"><span class="dot"></span><span>Willowmere<br>Collective</span></div>
  <div class="abs hero-photo" role="img" aria-label="Photo of a hooded figure sitting slumped in front of an old arched wooden door in a stone wall"></div>

  <div class="frame-line" style="left:32px;top:105px;width:5px;height:330px;"></div>
  <div class="frame-line" style="left:22px;top:430px;width:523px;height:5px;"></div>
  <div class="frame-line" style="left:540px;top:345px;width:5px;height:90px;"></div>

  <h1 class="abs title bebas">
    <span class="light">Behind</span>
    <span class="dark">Closed</span>
    <span class="light">Doors</span>
  </h1>
  <p class="abs tagline bebas">Break destructive relationship patterns<br>and learn how to create more love and intimacy</p>

  <dl class="abs info-table">
    <div class="info-row" style="height:58px;">
      <dt class="bebas">What is<br>intimacy?</dt>
      <dd><b>Intimacy is our emotional food</b> - it sustains and nourishes us, helping us feel connected, understood and valued. Lack of emotional intimacy in our most important relationships creates problems such as anxiety, jealously, withdrawal, betrayal, abandonment and even infidelity.</dd>
    </div>
    <div class="info-row" style="height:84px;">
      <dt class="bebas">Hunger<br>versus love.</dt>
      <dd><b>Emotional hunger is not love.</b> This hunger is a strong need caused by emotional deprivation in childhood. Feelings of emotional hunger are experienced as deep internal sensations that range in intensity from a dull ache to a sharp painful feeling. Because of its intensity, this sensation is often confused with real love. Many people claim to be loving and caring, when in fact they are actually feeling their emotional hunger and neediness. Emotional hunger is what we experience when feeling abandonment pain. This keeps us in unfulfilling, destructive &amp; addictive relationships.</dd>
    </div>
    <div class="info-row" style="height:94px;">
      <dt class="bebas">This program focuses<br>on abandonment and<br>engulfment issues.</dt>
      <dd>To avoid the pain of abandonment and the overwhelming feelings of engulfment, in childhood we subconsciously learn to create a fantasy bond. Later this bond is transferred to our adult relationships, especially romantic and sexual ones.<br><b>The fantasy bond is a primary defense against intimacy.</b><br>According to Dr. Alan Whitcombe, “the fantasy bond is a substitute for love and care that was missing in the child’s world. Many parents offer affection and love when they feel the need for it themselves. This type of physical affection drains the emotional resources of children rather than nourishing them. It is a form of taking, not giving.</dd>
    </div>
    <div class="info-row" style="height:76px;border-bottom:none;">
      <dt class="bebas small">Why is it important to<br>examine our childhood when<br>trying to sort out our issues<br>in adult relationships today?</dt>
      <dd style="border-bottom:none;"><b>Children are needy by nature, not by choice.</b> They instinctively adapt their behaviour and personalities in order to get their emotional needs met. As a result of the fantasy bond, created between child and caregiver, we carry with us into adulthood the same survival mechanisms leading to a sacrifice of our freedom and any real intimacy in loving relationships. Instead, we create dependencies with people, substances and behaviour patterns to fill the deep emptiness or loneliness within us.</dd>
    </div>
  </dl>
</section>

<!-- Back page -->
<section class="page page--back">
  <div class="frame-line" style="left:27px;top:32px;width:5px;height:325px;"></div>
  <div class="frame-line" style="left:27px;top:32px;width:107px;height:5px;"></div>
  <div class="frame-line" style="left:35px;top:352px;width:438px;height:5px;"></div>

  <h2 class="abs will-heading bebas">During this 5 days<br>intensive program<br>you will:</h2>
  <div class="abs child-photo" role="img" aria-label="Photo of a small child sitting against a weathered wooden wall with head resting on knees"></div>

  <ul class="abs outcomes">
    <li>Identify what you need to do for yourself to stop destructive relationship patterns.</li>
    <li>Learn how to protect yourself from feeling overwhelmed or drained in close relationships.</li>
    <li>Release emotional baggage from past adult relationships.</li>
    <li>Significantly heal childhood abandonment and engulfment issues.</li>
    <li>Identify the subconscious negative beliefs that are sabotaging you from having the relationship you desire.</li>
    <li>Release childhood trauma out of your body from abuse and neglect</li>
    <li>Learn how to set healthy boundaries - physically, emotionally, spiritually, intellectually and sexually.</li>
    <li>Differentiate between needs and values - the drivers in relationships.</li>
    <li>Identify your needs and values and determine steps to take to meet them.</li>
    <li>Free yourself of shame, guilt and fear from childhood and adult relationships.</li>
    <li>Communicate your needs and ask for what you want without feeling too embarrassed or vulnerable.</li>
    <li>Create healthy self-esteem and love - the foundation for intimacy.</li>
  </ul>

  <div class="abs back-corner-brand"><span class="dot"></span><span>Willowmere</span></div>

  <article class="card card--details">
    <h3 class="bebas">Program Details</h3>
    <h3 class="bebas">When:</h3>
    <table class="schedule">
      <tr><td>Thursday</td><td>25th October</td><td>6:00pm – 9:00pm</td></tr>
      <tr><td>Friday,</td><td>26th October</td><td>9:00pm – 5:00pm</td></tr>
      <tr><td>Saturday,</td><td>27th October</td><td>9:00pm – 9:00pm</td></tr>
      <tr><td>Sunday,</td><td>28th October</td><td>9:00pm – 5:00pm</td></tr>
      <tr><td>Monday,</td><td>29th October</td><td>9:00pm – 4:00pm</td></tr>
    </table>
    <h3 class="bebas">Enrollment Process:</h3>
    <p>This 5 day program is limited in numbers and offers individual and group time.<br><b>Enrolments close Friday, 19th October 2018.</b><br>To book your place, register your interest or find out more about this program please call<br><b>Marisol 0400 123 456</b><br>Out of town participants please contact our office for assistance with accommodation if required.</p>
  </article>

  <article class="card card--inclusions">
    <h3 class="bebas">Inclusions</h3>
    <ul class="bullets">
      <li>A pre-assessment phone consult</li>
      <li>Relevant on online diagnostic survey’s</li>
      <li>Integrated Equine Assisted Psychotherapy</li>
      <li>Ropes course</li>
      <li>All course materials (notebook, writing materials),</li>
      <li>Morning and afternoon tea daily.</li>
    </ul>
    <h3 class="bebas" style="margin-top:4px;">Investments</h3>
    <div class="price">$2250 including GST</div>
    <h3 class="bebas">Terms &amp; Conditions</h3>
    <ul class="bullets">
      <li>A non-refundable deposit of $500 is required to hold your place.</li>
      <li><b>Enrolments with full payment is required by Tuesday, 23th October 2018.</b></li>
      <li>Charge card transactions incur a 3.3% merchant fee, standard credit cards 2.5%.</li>
      <li>Card terminal facility available.</li>
    </ul>
  </article>

  <footer class="abs footer-band">
    <div class="abs footer-brand"><span class="dot"></span><span>WILLOWMERE COLLECTIVE</span></div>
    <div class="abs company">
      <h4>The Willowmere Collective Pty Ltd.</h4>
      <p class="indent">ABN 12 345 678 901</p>
      <p><svg viewBox="0 0 10 10"><path d="M5 0.5a3.3 3.3 0 0 0-3.3 3.3C1.7 6.2 5 9.5 5 9.5s3.3-3.3 3.3-5.7A3.3 3.3 0 0 0 5 0.5zm0 4.6a1.3 1.3 0 1 1 0-2.6 1.3 1.3 0 0 1 0 2.6z" fill="#c9c2b4"/></svg>42 Fernbrook Road, Hillcrest NSW 2790</p>
      <p><svg viewBox="0 0 10 10"><path d="M2.2 0.8l1.4 1.9-.8 1.1c.6 1.2 1.3 1.9 2.5 2.5l1.1-.8 1.9 1.4-.7 1.9C4.6 8.6 1.4 5.4.3 1.5z" fill="#c9c2b4"/></svg>Phone: 0400 123 456</p>
      <p><svg viewBox="0 0 10 10"><rect x="0.7" y="2" width="8.6" height="6" rx=".6" fill="none" stroke="#c9c2b4" stroke-width="1"/><path d="M1 2.4l4 3 4-3" fill="none" stroke="#c9c2b4" stroke-width="1"/></svg>Email: marisol@willowmerecollective.example</p>
    </div>
  </footer>
</section>

</body>
</html>
```